Harbortail Keepers Florida Retractable Banner Design

Looking for a fresh, modern, eye catching yet informative retractable banner design for our vendor booth events.

Our color scheme is teal, dark yellow, black, and white

Would like to include our services of Overnights, Pop in Visits, Dog Walking, Transport, and Attendants. We are veterinary professionals that offer a higher tier level of pet care.

Our tagline is Raising the Bar in Harbortail Animal Care

Require logo to be incorporated

Would like our images used or included

Would like to include that we offer law enforcement and military discounts

www.harbortailkeepers.net is our website
An example of our print marketing materials attached

```html
<!DOCTYPE html>
<html lang="en">
<head>
<meta charset="utf-8">
<title>Harbortail Keepers Florida – Retractable Banner</title>
<link href="https://fonts.googleapis.com/css2?family=Poppins:wght@300;400;500;600;700&family=Oswald:wght@600;700&display=swap" rel="stylesheet">
<style>
  :root{
    --ink:#1c2a2a;
    --ink-soft:#2a3b3b;
    --teal:#3fc1bd;
    --teal-deep:#2a9a96;
    --gold:#f2b300;
    --gold-deep:#e8a400;
    --paper:#f1f2f2;
    --white:#ffffff;
    --stage:#e9e9e6;
  }
  *{box-sizing:border-box;margin:0;padding:0}
  html,body{width:1200px;height:2709px;overflow:hidden;background:var(--stage)}
  body{font-family:"Poppins",sans-serif;position:relative}
  .banner{position:absolute;left:50px;top:51px;width:1100px;height:2607px;background:var(--paper);overflow:hidden;box-shadow:0 10px 30px rgba(0,0,0,.25)}
  .hero{position:absolute;left:0;top:0;width:1100px;height:1215px;background:radial-gradient(ellipse at 50% 40%,#233434 0%,var(--ink) 70%)}
  .abs{position:absolute}
  .brand-dot{left:470px;top:110px;width:160px;height:160px;border-radius:50%;background:var(--teal)}
  .brand-name{left:0;width:1100px;top:372px;text-align:center;font-weight:600;font-size:64px;color:var(--gold);letter-spacing:1px;line-height:1.1}
  .brand-services{left:0;width:1100px;top:470px;text-align:center;font-weight:500;font-size:28px;color:var(--teal);letter-spacing:6px}
  .tag-top{left:0;width:1100px;top:568px;text-align:center;font-weight:300;font-size:66px;color:var(--gold);letter-spacing:1px}
  .tag-band{left:230px;width:640px;top:666px;height:70px;background:var(--teal);text-align:center;font-weight:600;font-size:56px;line-height:70px;color:var(--white)}
  .headline{left:0;width:1100px;top:752px;height:190px;display:flex;align-items:center;justify-content:center;gap:18px}
  .pet-art{flex:0 0 104px;height:104px;border-radius:50%;background:linear-gradient(135deg,var(--teal),var(--teal-deep))}
  .tag-big{font-family:"Oswald",sans-serif;font-weight:700;font-size:150px;line-height:190px;letter-spacing:-2px;white-space:nowrap}
  .tag-big .t{color:var(--teal)} .tag-big .w{color:var(--white)}
  .intro{left:150px;width:800px;top:981px;height:115px;background:var(--ink-soft);border-radius:6px;text-align:center;font-size:38px;line-height:52px;padding-top:6px;color:var(--white)}
  .wave{left:0;top:1170px;width:1100px;height:70px}
  .services-bg{left:0;top:1215px;width:1100px;height:1196px;background:linear-gradient(180deg,#eceeee,#f5f6f6)}
  .services-title{left:317px;width:466px;top:1294px;height:77px;background:var(--ink);color:var(--white);font-weight:500;font-size:52px;line-height:80px;text-align:center}
  .svc{width:300px;text-align:center}
  .svc .ring{width:132px;height:132px;margin:0 auto;border-radius:50%;background:var(--white);box-shadow:0 3px 8px rgba(0,0,0,.25);display:flex;align-items:center;justify-content:center}
  .svc .disc{width:116px;height:116px;border-radius:50%;background:var(--teal);border:5px solid var(--teal-deep);display:flex;align-items:center;justify-content:center}
  .svc .label{margin-top:20px;font-weight:600;font-size:38px;color:var(--ink)}
  .gallery{left:73px;top:1869px;width:953px;height:297px;background:#a9adad;padding:12px;display:flex;gap:12px}
  .gallery .shot{flex:1;height:273px}
  .shot-gear{background:linear-gradient(135deg,#2f7a2a,#3d8d34 60%,#2c6a25)}
  .shot-keeper{background:linear-gradient(135deg,#3a2a28,#a67b6d 55%,#e9c1c6)}
  .shot-rest{background:linear-gradient(135deg,#cfcaca,#8a6a5c 55%,#e2dede)}
  .offer{left:91px;top:2202px;width:919px;height:159px;background:var(--ink);border-radius:8px;overflow:hidden}
  .offer .bar-top,.offer .bar-bot{position:absolute;left:34px;width:380px;height:12px;background:var(--teal)}
  .offer .bar-top{top:0}.offer .bar-bot{bottom:0}
  .offer .head{position:absolute;left:42px;top:10px;font-family:"Oswald",sans-serif;font-weight:700;font-size:98px;line-height:140px;color:var(--gold);white-space:nowrap}
  .offer .note{position:absolute;left:510px;top:34px;width:360px;height:92px;background:var(--white);border-radius:4px;font-weight:500;font-size:35px;line-height:40px;color:var(--ink);padding:6px 20px}
  .offer .note:before{content:"";position:absolute;left:-14px;top:30px;border:16px solid transparent;border-right:14px solid var(--white);border-left:0}
  .footer{left:0;top:2411px;width:1100px;height:196px;background:linear-gradient(90deg,var(--gold-deep),var(--gold),var(--gold-deep))}
  .url{left:0;width:1100px;top:2468px;text-align:center;font-weight:600;font-size:54px;color:var(--ink)}
</style>
</head>
<body>
<main class="banner">
  <section class="hero">
    <div class="abs brand-dot"></div>
    <h1 class="abs brand-name">HARBORTAIL KEEPERS</h1>
    <p class="abs brand-services">OVERNIGHTS - POP IN VISITS - DOG WALKING</p>
    <p class="abs tag-top">RAISING THE BAR</p>
    <p class="abs tag-band">IN HARBORTAIL</p>
    <div class="abs headline">
      <div class="pet-art" role="img" aria-label="Teal dog silhouette beside the headline"></div>
      <p class="tag-big"><span class="t">ANIMAL</span> <span class="w">CARE</span></p>
    </div>
    <p class="abs intro">We are veterinary professionals that<br>offer a higher tier level of pet care.</p>
  </section>

  <div class="abs services-bg" role="img" aria-label="Faded photo of pets resting at home behind the services"></div>
  <svg class="abs wave" viewBox="0 0 1100 70" preserveAspectRatio="none">
    <path d="M0 0H1100V40 Q1072 12 1045 40 T990 40 T935 40 T880 40 T825 40 T770 40 T715 40 T660 40 T605 40 T550 40 T495 40 T440 40 T385 40 T330 40 T275 40 T220 40 T165 40 T110 40 T55 40 T0 40Z" fill="#1c2a2a"/>
    <path d="M0 40 Q27 12 55 40 T110 40 T165 40 T220 40 T275 40 T330 40 T385 40 T440 40 T495 40 T550 40 T605 40 T660 40 T715 40 T770 40 T825 40 T880 40 T935 40 T990 40 T1045 40 T1100 40" fill="none" stroke="#b9bebe" stroke-width="8"/>
  </svg>

  <h2 class="abs services-title">OUR SERVICES</h2>

  <div class="abs svc" style="left:58px;top:1417px">
    <div class="ring"><div class="disc"><svg width="62" height="62" viewBox="0 0 24 24" fill="#fff"><path d="M3 11 12 4l9 7v9h-6v-6H9v6H3z"/></svg></div></div>
    <p class="label">OVERNIGHTS</p>
  </div>
  <div class="abs svc" style="left:400px;top:1417px">
    <div class="ring"><div class="disc"><svg width="62" height="62" viewBox="0 0 24 24" fill="#fff"><path d="M12 2a7 7 0 0 1 7 7c0 5-7 13-7 13S5 14 5 9a7 7 0 0 1 7-7zm0 4a3 3 0 1 0 0 6 3 3 0 0 0 0-6z"/></svg></div></div>
    <p class="label">POP IN VISITS</p>
  </div>
  <div class="abs svc" style="left:722px;top:1417px">
    <div class="ring"><div class="disc"><svg width="62" height="62" viewBox="0 0 24 24" fill="#fff"><circle cx="8" cy="4" r="2"/><path d="M7 7h3l2 5-2 1-1-2-1 4 2 5H8l-2-5 1-6-2 3H3z"/><path d="M14 16h6l1-2 1 1-1 2v4h-1v-3h-5v3h-1z"/></svg></div></div>
    <p class="label">DOG WALKING</p>
  </div>
  <div class="abs svc" style="left:224px;top:1629px">
    <div class="ring"><div class="disc"><svg width="62" height="62" viewBox="0 0 24 24" fill="#fff"><path d="M3 6h12v10H3zM16 9h3l3 4v3h-6z"/><circle cx="7" cy="18" r="2"/><circle cx="18" cy="18" r="2"/></svg></div></div>
    <p class="label">TRANSPORT</p>
  </div>
  <div class="abs svc" style="left:559px;top:1629px">
    <div class="ring"><div class="disc"><svg width="62" height="62" viewBox="0 0 24 24" fill="#fff"><path d="M3 5h16v6h-2V9H5v10h7v2H3z"/><path d="M7 11h2v2H7zm4 0h2v2h-2zm-4 4h2v2H7z"/><circle cx="18" cy="17" r="4.5" fill="none" stroke="#fff" stroke-width="2"/><path d="M18 15v2.5h1.8" stroke="#fff" stroke-width="1.5" fill="none"/></svg></div></div>
    <p class="label">ATTENDANTS</p>
  </div>

  <div class="abs gallery">
    <div class="shot shot-gear" role="img" aria-label="Photo of a leash, frisbee and harness on grass"></div>
    <div class="shot shot-keeper" role="img" aria-label="Photo of a pet keeper holding a branded mug"></div>
    <div class="shot shot-rest" role="img" aria-label="Photo of a dog resting on a blanket"></div>
  </div>

  <div class="abs offer">
    <span class="bar-top"></span><span class="bar-bot"></span>
    <p class="head">WE OFFER</p>
    <p class="note">Enforcement and<br>Military Discounts</p>
  </div>

  <div class="abs footer"></div>
  <p class="abs url">www.harbortailkeepers.net</p>
</main>
</body>
</html>
```